"Maple Nook" needs a A5 flyer for its "Art Contest"

Maple Nook needs a double sided A5 Flyer that illustrates in a child-friendly look the following competition:

Search for the up and coming Bright Sprout. The aim of our Bright Sprout is to allow our children to explore the artist within them and motivate them to express their talents through the fine art of drawing and painting.

Description: I have an art school, "Maple Nook", where children of 3-5 years old attend and learn how to paint and draw. We are making a competition where each child gets to draw a picture which we will upload to Chirpwall and parents will vote for best picture. We need to distribute to the parents a flyer with following content.

Competition Name: Bright Sprout

Front Side (content):
No major text on the front. Only the Logo and messages grabbing the readers attention such as "Who will be our next Artist?", "Vote for your Child", "Like Us on our Chirpwall Page".

Back Side (content):
Back side content is divided into 3 sections:

Section1:
How it Works?
Every child of every class will participate. Photos will be grouped by class.
There will be a Bright Sprout for each class, and there will be a Bright Sprout for the school.

Section2:
How to Participate?
In our search for ‘Bright Sprout’, we will select one piece of artwork from each child in the school, photograph it and upload it to our Chirpwall page.
Vote for your favourite painting by following the steps below:
1- From your chirpwall account go to www.chirpwall.example/Maple Nook
and “Like Us” to become a fan
2- Click on the“Bright Sprout” from the application menu
3- Browse through the different classes and vote for each picture you like
4- Invite your friends to vote for the picture you like to increase the chances of winning
The artist of the painting with most “Likes” will be crowned ‘Bright Sprout’.

Section3:
Note (in the footer):
Please note that the winner’s photo will be displayed in our “Bright Sprout” Frame on our Chirpwall landing page. If you do not want your child’s photograph to be posted on our Chirpwall page in this manner, please let us know by sending an e-mail.
, Maple Nook needs a double sided A5 Flyer that illustrates in a child-friendly look the following competition:

Front Side (content):

Back Side (content):

Section1:
How it Works?

Section2:
How to Participate?

Section3:
Note (in the footer):

Reason: To give more time for improvements on submitted designs and if possible some additional submissions.

Target Market(s)

Parents of the children attending at our school, Parents of the children attending at our school

Industry/Entity Type

Painting

Requirements
Must have
• Colors used in the design should be strict to our logo colors. We have 4 colors in our logo feel free to use one or all of them through out the design:
#6CB53C
#DB2718
#5D9DD5
#F4D602

The elements in our logo are playful and hand drawn and written, so the flyer design should reflect the hand made style rather than solid elements and objects., Colors used in the design should be strict to our logo colors. We have 4 colors in our logo feel free to use one or all of them through out the design:
#6CB53C
#DB2718
#5D9DD5
#F4D602

The elements in our logo are playful and hand drawn and written, so the flyer design should reflect the hand made style rather than solid elements and objects.
Should not have
• Images of real children., Images of real children.

```html
<!DOCTYPE html>
<html lang="en">
<head>
<meta charset="utf-8">
<title>Maple Nook – Bright Sprout Competition</title>
<link href="https://fonts.googleapis.com/css2?family=Arvo:ital,wght@0,400;0,700;1,400&display=swap" rel="stylesheet">
<style>
  :root {
    --teal: #257a8a;
    --teal-band: #2a7a8c;
    --orange: #f7941d;
    --green: #6cb53c;
    --red: #db2718;
    --ink: #1e1e1e;
    --band-ink: #1f3a40;
    --muted: #8a8a8a;
    --paper: #ffffff;
  }
  * { margin: 0; padding: 0; box-sizing: border-box; }
  html, body { width: 1200px; height: 850px; overflow: hidden; background: var(--paper); }
  body { font-family: "Arvo", Georgia, serif; color: var(--ink); }

  .flyer { position: relative; width: 1200px; height: 850px; }

  /* Front side */
  .front { position: absolute; left: 0; top: 0; width: 600px; height: 850px; overflow: hidden; }
  .front__artwork {
    position: absolute; inset: 0;
    background:
      radial-gradient(circle at 60% 20%, rgba(236,120,50,.75) 0, rgba(236,120,50,0) 28%),
      radial-gradient(circle at 25% 70%, rgba(244,200,40,.55) 0, rgba(244,200,40,0) 30%),
      radial-gradient(circle at 80% 85%, rgba(219,80,40,.5) 0, rgba(219,80,40,0) 30%),
      radial-gradient(circle at 15% 25%, rgba(93,157,213,.45) 0, rgba(93,157,213,0) 30%),
      linear-gradient(160deg, #e9e4d8, #ddd6c6);
  }
  .front__brand {
    position: absolute; left: 60px; top: 330px;
    display: flex; align-items: center; gap: 18px;
  }
  .front__brand-dot { width: 44px; height: 44px; border-radius: 50%; background: var(--paper); }
  .front__brand-name { font-size: 70px; font-weight: 400; color: var(--paper); letter-spacing: 1px; }
  .front__band {
    position: absolute; left: 0; top: 660px; width: 601px; height: 98px;
    background: var(--teal-band);
    display: flex; align-items: center; justify-content: center;
  }
  .front__headline { font-size: 26px; letter-spacing: 1px; color: var(--band-ink); font-weight: 400; }

  /* Back side */
  .back { position: absolute; left: 640px; top: 0; width: 530px; height: 850px; }
  .back__title { position: absolute; top: 84px; left: 0; font-size: 33px; font-weight: 400; letter-spacing: .5px; white-space: nowrap; }
  .back__title-main { color: var(--teal); }
  .back__title-accent { color: var(--orange); }

  .section-heading { position: absolute; left: 1px; font-size: 21px; font-weight: 400; letter-spacing: .5px; }
  .section-heading--works { top: 154px; color: var(--green); }
  .section-heading--join { top: 250px; color: var(--red); }

  .body-text { position: absolute; left: 1px; font-size: 12.5px; line-height: 15.5px; color: var(--ink); }
  .body-text--works { top: 194px; width: 520px; }
  .body-text--join { top: 293px; width: 515px; line-height: 13px; letter-spacing: .5px; text-align: justify; }

  .steps { position: absolute; left: 27px; top: 350px; width: 490px; list-style: none; font-size: 12.5px; line-height: 15.5px; letter-spacing: .5px; }
  .steps__item { padding-left: 18px; text-indent: -18px; }
  .steps__item--1 { margin-bottom: 14px; }
  .steps__item--2 { margin-bottom: 15px; }
  .steps__item--3 { margin-bottom: 15px; }

  .tagline { position: absolute; top: 584px; left: 0; width: 512px; text-align: center; font-size: 20.5px; line-height: 24px; color: var(--teal); letter-spacing: .8px; }
  .tagline__likes { color: var(--red); }

  .footnote { position: absolute; top: 746px; left: 1px; width: 520px; font-size: 11px; line-height: 14px; font-style: italic; color: var(--muted); letter-spacing: .3px; }
</style>
</head>
<body>
<main class="flyer">
  <section class="front">
    <div class="front__artwork" role="img" aria-label="Colourful splattered children's paint artwork in orange, yellow, red, blue and green"></div>
    <div class="front__brand">
      <span class="front__brand-dot"></span>
      <span class="front__brand-name">Maple Nook</span>
    </div>
    <div class="front__band">
      <p class="front__headline">WHO WILL BE OUR NEXT ARTIST?</p>
    </div>
  </section>

  <section class="back">
    <h1 class="back__title"><span class="back__title-main">BRIGHT SPROUT</span> <span class="back__title-accent">COMPETITION</span></h1>

    <h2 class="section-heading section-heading--works">HOW IT WORKS?</h2>
    <p class="body-text body-text--works">Every child of every class will participate. Photos will be grouped by class.<br>There will be a Bright Sprout for each class, and there will be a<br>Bright Sprout for the school.</p>

    <h2 class="section-heading section-heading--join">HOW TO PARTICIPATE?</h2>
    <p class="body-text body-text--join">In our search for ‘Bright Sprout’, we will select one piece of artwork from each child in the school, photograph it and upload it to our Chirpwall page. Vote for your favourite painting by following the steps below:</p>

    <ol class="steps">
      <li class="steps__item steps__item--1">1 - From your chirpwall account go to www.chirpwall.example/Maple Nook and “Like Us” to become a fan</li>
      <li class="steps__item steps__item--2">2 - Click on the“Bright Sprout” from the application menu</li>
      <li class="steps__item steps__item--3">3 - Browse through the different classes and vote for each picture you like</li>
      <li class="steps__item">4 - Invite your friends to vote for the picture you like to increase the chances of winning</li>
    </ol>

    <p class="tagline">The artist of the painting with most “<span class="tagline__likes">Likes</span>”<br>will be crowned ‘Bright Sprout’.</p>

    <p class="footnote">Please note that the winner’s photo will be displayed in our “Bright Sprout” Frame on our Chirpwall landing page. If you do not want your child’s photograph to be posted on our Chirpwall page in this manner, please let us know by sending an e-mail.</p>
  </section>
</main>
</body>
</html>
```